Home loan promotion flyer (DL or Postcard)

We need a flyer that promotes our home loan broking service. In summary, we are an Australian financial planning business that helps Gen X and Y make better financial planning decisions.

We would like the design to have a similar look and feel to the following:
http://www.leaflet-vault.com.au/qmpr/bright_path_steady_living/

Text that I would like included is:

(HEADING) Awesome Debt Management: Someone else's money used to Your advantage.

(Paragraph) Debt is not necessarily a dirty work. Smart Australian investors often use debt strategies to minimise tax burdens, pay off their home loan sooner and to build their wealth quicker.

(Promotion) Bring this along to your COMPLIMENTARY finance health check and we will give you a $25 Durban Vale voucher to celebrate your first step towards a better financial future. (Please include the image of the voucher near this text).

Finally, you must include our number (1300 614 972) and website (www.qmpr.com.au)

Apart from being consistent with the e-brochure above (please ensure you view the link), we would like the design to be bold and stand out from the crowd.

I have attached a previous home loan promotion design that I like but I feel that there are too many words and not enough space. Please use the good elements but avoid the rest.

Finally, I've also attached a DL "goldfish" design that I really like because I think the design is memorable and stands-out.
Updates

Reason: Hi there designers Thanks for your designs so far. They look great. I have extended the brief to give everyone the opportunity to reassess their design to make sure that it is consistent with the design brief. If anything is unclear please don't hesitate to make contact. Thanks TR

Target Market(s)

Australian first home buyers and property investors.

Industry/Entity Type

Financial

Requirements
Must have
• The design MUST be consistent with the existing marketing material referred to in this link.

```html
<!DOCTYPE html>
<html lang="en">
<head>
<meta charset="utf-8">
<title>Awesome Debt Management – Flyer</title>
<link rel="stylesheet" href="https://fonts.googleapis.com/css2?family=Source+Sans+3:ital,wght@0,400;0,600;0,700;1,600&display=swap">
<style>
  :root {
    --page-bg: #e9e4dc;
    --ink: #0a0a0a;
    --white: #ffffff;
    --lime: #8cc63f;
    --green: #3aa64a;
    --grey-text: #222222;
    --promo-green: #9bd14a;
    --brick: #8e4a36;
    --skin: #ecc9ae;
    --denim: #a9c1d8;
  }
  * { margin: 0; padding: 0; box-sizing: border-box; }
  html, body {
    width: 1155px; height: 1200px; overflow: hidden;
    background: var(--page-bg);
    font-family: "Source Sans 3", "Myriad Pro", Arial, sans-serif;
  }
  .canvas { position: relative; width: 1155px; height: 1200px; }
  .card {
    position: absolute; left: 103px; width: 953px; height: 450px;
    border-radius: 14px; overflow: hidden;
    box-shadow: 0 4px 10px rgba(0,0,0,.25);
  }
  .card--front { top: 103px; background: var(--ink); }
  .card--back  { top: 611px; background: var(--white); }
  .card-shapes { position: absolute; inset: 0; }

  /* front */
  .headline {
    position: absolute; left: 47px; width: 450px; top: 26px;
    text-align: center; color: var(--white);
    font-weight: 700; font-size: 60px; line-height: 58px;
  }
  .tagline {
    position: absolute; left: 47px; width: 450px; top: 155px;
    text-align: center; color: var(--lime);
    font-size: 19px; font-weight: 400;
  }
  .brand {
    position: absolute; left: 47px; width: 450px; top: 242px;
    display: flex; flex-direction: column; align-items: center; gap: 16px;
  }
  .brand-square { width: 100px; height: 100px; background: var(--green); }
  .brand-name { color: var(--white); font-weight: 700; font-size: 25px; }
  .intro {
    position: absolute; left: 519px; top: 30px; width: 200px;
    color: var(--ink); font-size: 20px; line-height: 33.5px;
  }

  /* back */
  .contact {
    position: absolute; left: 121px; top: 362px;
    color: var(--ink); font-size: 21px;
  }
  .contact strong { font-size: 28px; font-weight: 700; }
  .web {
    position: absolute; left: 187px; top: 405px; width: 160px;
    text-align: center; color: var(--grey-text);
    font-size: 14px; letter-spacing: 2px;
  }
  .back-square { position: absolute; left: 24px; top: 342px; width: 70px; height: 78px; background: var(--green); }
  .promo {
    position: absolute; left: 505px; top: 34px; width: 200px;
    text-align: center; color: var(--promo-green);
    font-style: italic; font-weight: 600; font-size: 21px; line-height: 32px;
  }
</style>
</head>
<body>
<div class="canvas">

  <section class="card card--front">
    <svg class="card-shapes" width="953" height="450" viewBox="0 0 953 450">
      <defs>
        <linearGradient id="panelGreen" x1="0" y1="0" x2="1" y2="0">
          <stop offset="0" stop-color="#7fbf35"/>
          <stop offset="1" stop-color="#a8d84c"/>
        </linearGradient>
      </defs>
      <rect class="edge-band" x="0" y="0" width="47" height="450" fill="var(--lime)"/>
      <path class="photo-shadow" d="M700,0 H953 V450 H560 C660,440 720,410 735,350 Z" fill="var(--ink)"/>
      <path class="house-photo" role="img" aria-label="Photo of a red-brick two-storey family home with a green lawn"
            d="M731,0 H953 V450 H640 C705,438 738,405 745,352 L745,0 Z" fill="var(--brick)"/>
      <path class="intro-panel" d="M497,0 H731 V330 C718,395 650,430 540,450 H497 Z" fill="url(#panelGreen)"/>
    </svg>
    <h1 class="headline">Awesome Debt<br>Management</h1>
    <p class="tagline">someone else's money used to&nbsp; your advantage</p>
    <div class="brand">
      <span class="brand-square"></span>
      <span class="brand-name">Quarry Mile Planning</span>
    </div>
    <p class="intro">Debt is not<br>necessarily a dirty<br>work. Smart<br>Australian investors<br>often use debt<br>strategies to<br>minimise tax<br>burdens, pay off<br>their home loan<br>sooner and to build<br>their wealth quicker.</p>
  </section>

  <section class="card card--back">
    <svg class="card-shapes" width="953" height="450" viewBox="0 0 953 450">
      <rect class="hands-photo" role="img" aria-label="Photo of two open hands holding a small model house with a red roof"
            x="60" y="0" width="420" height="320" rx="10" fill="var(--skin)"/>
      <path class="promo-stripe" d="M497,0 H735 V360 C728,425 680,448 632,450 H497 Z" fill="var(--lime)"/>
      <path class="promo-panel" d="M497,0 H713 V360 C705,420 660,445 610,450 H497 Z" fill="var(--ink)"/>
      <rect class="family-photo" role="img" aria-label="Photo of a smiling family of four standing together"
            x="748" y="10" width="190" height="430" rx="10" fill="var(--denim)"/>
    </svg>
    <span class="back-square"></span>
    <p class="contact">Contact us - <strong>(1300 614 972)</strong></p>
    <p class="web">www.qmpr.com.au</p>
    <p class="promo">Bring this<br>along to your<br>COMPLIMENTARY<br>finance health<br>check and we will<br>give you a $25<br>Durban Vale<br>voucher to<br>celebrate your first<br>step towards a<br>better financial<br>future.</p>
  </section>

</div>
</body>
</html>
```